Real estate business card

I need a business card for my real estate company. I help clients buy and sell properties. I would like to keep the design very simple and professional. I would like the design to convey professionalism, safety and trust. I prefer no graphics but a simple logo design would be nice if that is part of what you do.
Updates

Please keep the designs simple. No high-rise buildings please. 

Target Market(s)

Age group 30-60 mostly affluent

Industry/Entity Type

Real Estate

Contact Information for Business Card

Venkell Realtors
Bernard Venkell, Broker
5146 Marrow Ave. #327, La Crescenta, CA 91214

Requirements
Nice to have
• Logo can be combination of my initials BV or just Z or a simple geometric shape? Please see "Desig Ideas" attachment. No pics of houses or shaking hands, dollar bills, $, %, etc...
Please use fonts similar to Helvetica for a clean, modern look (think Northern European design, simple, clean yet bold)

Also use font colors such as blue, grey in different shades. Use pastel colors if better.

```html
<!DOCTYPE html>
<html lang="en">
<head>
<meta charset="utf-8">
<title>Venkell Realtors – Business Card</title>
<link rel="stylesheet" href="https://fonts.googleapis.com/css2?family=Arimo:wght@400&display=swap">
<style>
  :root {
    --teal: #238d96;
    --lime: #86e80c;
    --aqua: #52dfcb;
    --charcoal: #363c39;
    --ink: #1f2221;
    --paper: #ffffff;
  }
  html, body {
    margin: 0;
    padding: 0;
    width: 1200px;
    height: 702px;
    overflow: hidden;
    background: var(--paper);
  }
  .card {
    position: relative;
    width: 1200px;
    height: 702px;
    background: var(--paper);
    font-family: "Arimo", Helvetica, Arial, sans-serif;
    font-weight: 400;
    line-height: 1;
    overflow: hidden;
  }
  .card > * { position: absolute; margin: 0; white-space: nowrap; }

  .contact { right: 85px; text-align: right; }
  .contact--license { top: 67px; font-size: 22px; color: var(--teal); }
  .contact--phone { top: 101px; font-size: 27px; color: var(--ink); }
  .contact--email { top: 140px; font-size: 27px; color: var(--ink); }

  .brand-square {
    left: 0; top: 273px;
    width: 61px; height: 120px;
    background: var(--lime);
  }
  .brand-name { left: 92px; color: var(--teal); }
  .brand-name--primary { top: 283px; font-size: 58px; }
  .brand-name--secondary { left: 83px; top: 359px; font-size: 42px; text-transform: uppercase; }

  .name-band {
    left: 620px; top: 273px;
    width: 580px; height: 120px;
    background: var(--charcoal);
  }
  .name-band__accent {
    left: 1145px; top: 273px;
    width: 27px; height: 120px;
    background: var(--aqua);
  }
  .agent-name {
    left: 671px; top: 304px;
    font-size: 57px;
    color: var(--lime);
  }

  .address {
    right: 74px; top: 460px;
    font-size: 40px;
    line-height: 51.5px;
    text-align: right;
    color: var(--ink);
    font-style: normal;
  }
</style>
</head>
<body>
  <main class="card">
    <p class="contact contact--license">CA BRE 01473528</p>
    <p class="contact contact--phone">(818) 555-0186</p>
    <p class="contact contact--email">hello@venkellrealtors.example</p>

    <div class="brand-square" aria-hidden="true"></div>
    <p class="brand-name brand-name--primary">Venkell</p>
    <p class="brand-name brand-name--secondary">Realtors</p>

    <div class="name-band" aria-hidden="true"></div>
    <div class="name-band__accent" aria-hidden="true"></div>
    <h1 class="agent-name" style="font-weight:400;">Bernard Venkell</h1>

    <address class="address">Broker 5146 Marrow Ave.,<br>#327, La Crescenta,<br>CA 91214</address>
  </main>
</body>
</html>
```